Need a New "Register to Download" Graphic

You're the artist! Please get creative and if you think you can make something look better for our front page do so, get our attention and make us pick you!

Currently we have a "Buy Now" button on our website and we want to change this to say "Register to Download" the image must be the same size as the current attached button and be in the form of .png

Do not put any CoinLark or credit card info on the image

On the current image where the CoinLark info is wwritten replace it with "Registration Only Takes 2 Minutes!"

For extra points and to get select you can also change the box graphic on the back and make the "Get Instant Access" look better.

See current graphics http://www.grabtrickly.example
Updates

Project Deadline Extended
Reason: Looking for more submissions

Just made a guarantee on payment, thanks guys! Still waiting for more designs before we choose.

Target Market(s)

Men 18 - 26

Industry/Entity Type

Credit Card

Font styles to use
Sans Serif

Requirements
Must have
• Must blend with website

```html
<!DOCTYPE html>
<html lang="en">
<head>
<meta charset="utf-8">
<title>Register to Download</title>
<link rel="stylesheet" href="https://fonts.googleapis.com/css2?family=Rubik+Dirt&family=Roboto+Condensed:ital,wght@1,700&display=swap">
<style>
  :root {
    --page-bg: #ffffff;
    --panel-dark: #4a0608;
    --panel-mid: #c3161c;
    --arrow-red: #e0151b;
    --frame-light: #f2f2f2;
    --frame-dark: #8a8a8a;
    --button-red: #9c0e12;
    --button-dark: #5a0609;
    --headline-white: #ffffff;
    --accent-yellow: #fff200;
    --tagline-blue: #1d5597;
  }
  html, body {
    margin: 0;
    padding: 0;
    overflow: hidden;
    background: var(--page-bg);
  }
  .canvas {
    position: relative;
    width: 915px;
    height: 1200px;
    overflow: hidden;
    background: var(--page-bg);
  }
  .panel {
    position: absolute;
    left: 224px;
    top: 136px;
    width: 466px;
    height: 926px;
    background:
      radial-gradient(ellipse 75% 45% at 50% 55%, var(--panel-mid) 0%, #a51217 55%, var(--panel-dark) 100%);
  }
  .headline {
    position: absolute;
    left: 224px;
    top: 268px;
    width: 466px;
    margin: 0;
    text-align: center;
    font-family: "Rubik Dirt", "Arial Black", sans-serif;
    font-weight: 400;
    font-size: 92px;
    line-height: 100px;
    letter-spacing: 1px;
    color: var(--headline-white);
    text-shadow: 3px 4px 4px rgba(0,0,0,0.55);
    transform: scaleX(0.86);
    transform-origin: 50% 0;
  }
  .arrows {
    position: absolute;
    left: 0;
    top: 0;
  }
  .cta-button {
    position: absolute;
    left: 160px;
    top: 737px;
    width: 590px;
    height: 156px;
    box-sizing: border-box;
    border-radius: 8px;
    padding: 11px;
    background: linear-gradient(180deg, var(--frame-light), #c8c8c8 45%, var(--frame-dark) 55%, #e6e6e6);
    box-shadow: 0 3px 6px rgba(0,0,0,0.35);
  }
  .cta-face {
    width: 100%;
    height: 100%;
    border-radius: 4px;
    overflow: hidden;
    background: linear-gradient(180deg, var(--button-dark), var(--button-red) 30%, var(--button-red) 70%, var(--button-dark));
    display: flex;
    align-items: center;
    justify-content: center;
  }
  .cta-label {
    display: inline-block;
    font-family: "Rubik Dirt", "Arial Black", sans-serif;
    font-size: 54px;
    line-height: 1;
    padding-top: 10px;
    color: var(--headline-white);
    text-shadow: 2px 3px 3px rgba(0,0,0,0.6);
    white-space: nowrap;
    transform: scaleX(0.78);
    transform-origin: 50% 50%;
  }
  .cta-label .highlight {
    color: var(--accent-yellow);
  }
  .tagline {
    position: absolute;
    left: 303px;
    top: 718px;
    margin: 0;
    font-family: "Roboto Condensed", "Arial Narrow", sans-serif;
    font-style: italic;
    font-weight: 700;
    font-size: 32px;
    line-height: 40px;
    letter-spacing: 0.3px;
    color: var(--tagline-blue);
    white-space: nowrap;
    text-shadow: -2px -2px 0 #fff, 2px -2px 0 #fff, -2px 2px 0 #fff, 2px 2px 0 #fff, 0 2px 0 #fff, 0 -2px 0 #fff, 2px 0 0 #fff, -2px 0 0 #fff;
  }
</style>
</head>
<body>
<div class="canvas">
  <div class="panel"></div>

  <h1 class="headline">GET<br>INSTANT<br>ACCESS</h1>

  <svg class="arrows" width="915" height="1200" viewBox="0 0 915 1200" aria-hidden="true">
    <g class="arrow arrow-upper">
      <path d="M 218 762 C 158 740 150 690 200 670 C 235 656 275 662 300 674" fill="none" stroke="#ffffff" stroke-width="40" stroke-linecap="round"/>
      <polygon points="284,628 342,690 268,710" fill="#ffffff" stroke="#ffffff" stroke-width="10" stroke-linejoin="round"/>
      <path d="M 218 762 C 158 740 150 690 200 670 C 235 656 275 662 300 674" fill="none" stroke="var(--arrow-red)" stroke-width="28" stroke-linecap="round"/>
      <polygon points="284,628 342,690 268,710" fill="var(--arrow-red)"/>
    </g>
    <g class="arrow arrow-lower">
      <path d="M 716 880 C 762 900 768 950 722 966 C 690 976 650 970 620 958" fill="none" stroke="#ffffff" stroke-width="40" stroke-linecap="round"/>
      <polygon points="626,918 566,948 602,1002" fill="#ffffff" stroke="#ffffff" stroke-width="10" stroke-linejoin="round"/>
      <path d="M 716 880 C 762 900 768 950 722 966 C 690 976 650 970 620 958" fill="none" stroke="var(--arrow-red)" stroke-width="28" stroke-linecap="round"/>
      <polygon points="626,918 566,948 602,1002" fill="var(--arrow-red)"/>
    </g>
  </svg>

  <div class="cta-button">
    <div class="cta-face">
      <span class="cta-label">Register to <span class="highlight">Download!</span></span>
    </div>
  </div>

  <p class="tagline">Registration Only Takes 2 Minutes!</p>
</div>
</body>
</html>
```